TRENDY & MODERN BUSINESS CARD DESIGN for Media Company *

I need a minimalistic - clean - modern and professional business card layout and design for MEDIA & PHOTOGRAPHY STUDIO.

We do NOT have a logo, and not really looking for one - but rather excellent typography and design. We would consider the 3 as a focal point.

We do personal and commercial photography.

Target Market(s)

Personal and commercial photography clientele

Contact Information for Business Card

ZUB size - from zub.com / size guidelines are enclosed in the brief

Font styles to use
Sans Serif

Colors
f78f20
eda3c7
cee9f5
0555a3
e667a6
fbf289

Requirements
Must have
• Clean lines - Modern layout
Nice to have
• All blue background as an option - use color palette in brief please.
Should not have
• Old fashion fonts and regular fonts.

```html
<!DOCTYPE html>
<html lang="en">
<head>
<meta charset="utf-8">
<title>Halden Studio — Business Card</title>
<link rel="stylesheet" href="https://fonts.googleapis.com/css2?family=Roboto:wght@300;400;700;900&family=Caveat:wght@400&display=swap">
<style>
  :root {
    --stage: #232323;
    --card-light: #1b64b3;
    --card-mid: #1a56a2;
    --card-dark: #164a8f;
    --ink: #ffffff;
    --accent-yellow: #fbf289;
    --wave-tint: #2a6fbe;
  }
  * { box-sizing: border-box; margin: 0; padding: 0; }
  html, body {
    width: 1200px; height: 1200px; overflow: hidden;
    background: var(--stage);
    font-family: "Roboto", Arial, sans-serif;
    color: var(--ink);
  }
  .card-set {
    position: absolute; inset: 0;
    display: flex; justify-content: center; align-items: center; gap: 60px;
  }
  .card {
    position: relative;
    width: 480px; height: 840px;
    background: radial-gradient(ellipse at 50% 45%, var(--card-light) 0%, var(--card-mid) 55%, var(--card-dark) 100%);
    box-shadow: 0 14px 30px rgba(0,0,0,0.55);
    display: flex; flex-direction: column; align-items: center;
    text-align: center;
  }
  .card--back { justify-content: center; }
  .card__pattern {
    position: absolute; inset: 0;
    background: linear-gradient(135deg, var(--wave-tint) 0%, var(--card-mid) 50%, var(--wave-tint) 100%);
    opacity: 0.55;
  }
  .brand { position: relative; display: flex; flex-direction: column; align-items: center; }
  .brand__name {
    font-weight: 300; font-size: 44px; letter-spacing: 1px; line-height: 1;
  }
  .brand__tagline {
    font-family: "Caveat", cursive;
    font-size: 28px; margin-top: 8px;
    display: flex; align-items: center; gap: 8px;
  }
  .brand__dot { width: 9px; height: 9px; border-radius: 50%; background: var(--ink); }
  .card--front { padding-top: 230px; }
  .person { margin-top: 34px; }
  .person__name { font-weight: 900; font-size: 29px; letter-spacing: 0.3px; line-height: 1.05; }
  .person__title { color: var(--accent-yellow); font-size: 18px; font-weight: 400; margin-top: 4px; }
  .divider { width: 16px; height: 2px; background: var(--ink); margin: 22px auto; }
  .contact { font-size: 19px; font-weight: 400; line-height: 1.4; font-style: normal; }
  .locations__label { font-weight: 700; font-size: 19px; }
  .locations__list { font-size: 19px; line-height: 1.4; }
</style>
</head>
<body>
  <main class="card-set">
    <section class="card card--back">
      <div class="card__pattern" role="img" aria-label="Subtle wavy line pattern across the card background"></div>
      <div class="brand">
        <p class="brand__name">HALDEN STUDIO</p>
        <p class="brand__tagline">Framing Moments <span class="brand__dot"></span> Telling Stories</p>
      </div>
    </section>

    <section class="card card--front">
      <div class="brand">
        <p class="brand__name">HALDEN STUDIO</p>
        <p class="brand__tagline">Framing Moments <span class="brand__dot"></span> Telling Stories</p>
      </div>
      <div class="person">
        <p class="person__name">MARISOL VEGA</p>
        <p class="person__title">FOUNDER &amp; MEDIA DIRECTOR</p>
      </div>
      <div class="divider"></div>
      <address class="contact">
        2040 Harbor Avenue, Suite 4<br>Tampa, FL 33602
      </address>
      <div class="divider"></div>
      <p class="contact">(813) 555-0142<br>mari@haldenstudio.com</p>
      <div class="divider"></div>
      <div class="locations">
        <p class="locations__label">Studios</p>
        <p class="locations__list">Tampa | Austin | Denver<br>Lima | Porto</p>
      </div>
    </section>
  </main>
</body>
</html>
```